Wedding Photography business card

I need a business card made for a wedding photography business. Formal, unique, i like dark colors maybe black, white, gray, deep blue, silver. Sharp.

This is an idea i have i don't know if it would work.
Think Palm Beach, florida

work in mirror mode in your design program, Just an idea

Front side:
feminine, classy maybe white from wedding dress,
script, elegant,

back side:
masculine, black from tux, symbolizing strength, power,
serif

RK Photography
(561) 430-2917
www.rolfkphoto.example

Target Market(s)

upscale Weddings, targeting bride and groom

Industry/Entity Type

Wedding

Font styles to use
Serif
Script

Colors

Designer to choose colors to be used in the design.

Requirements
Must have
• both sides match somehow

```html
<!DOCTYPE html>
<html lang="en">
<head>
<meta charset="utf-8">
<title>RK Photography – Business Card</title>
<link rel="stylesheet" href="https://fonts.googleapis.com/css2?family=Cormorant+Garamond:wght@400;500&display=swap">
<style>
  :root {
    --page-bg: #ffffff;
    --ink: #151515;
    --card-black: #0c0c0c;
    --frame-black: #0a0a0a;
    --silver-light: #f2f2f2;
    --silver-mid: #a9a9a9;
    --silver-dark: #5e5e5e;
    --backdrop-light: #eef0f4;
    --backdrop-dark: #c9ced7;
    --contact-text: #cfcfcf;
  }
  * { box-sizing: border-box; margin: 0; padding: 0; }
  html, body {
    width: 1200px;
    height: 900px;
    overflow: hidden;
    background: var(--page-bg);
  }
  .canvas {
    width: 1200px;
    height: 900px;
    display: flex;
    align-items: center;
    justify-content: center;
    gap: 60px;
  }
  .card {
    position: relative;
    width: 520px;
    height: 300px;
    border-radius: 24px;
    overflow: hidden;
  }

  /* Front side */
  .card--front {
    border: 2px solid #e3e5ea;
  }
  .front-backdrop {
    position: absolute;
    inset: 0;
    background: radial-gradient(ellipse at 50% 45%, var(--backdrop-light) 0%, var(--backdrop-dark) 100%);
  }
  .front-frame {
    position: absolute;
    inset: 6px;
    border: 6px solid var(--frame-black);
    border-radius: 20px;
  }
  .front-brand {
    position: absolute;
    inset: 0;
    display: flex;
    flex-direction: column;
    align-items: center;
    justify-content: center;
    gap: 16px;
  }
  .brand-circle {
    width: 84px;
    height: 84px;
    border: 3px solid var(--ink);
    border-radius: 50%;
  }
  .brand-name {
    font-family: "Cormorant Garamond", serif;
    font-weight: 500;
    font-size: 27px;
    letter-spacing: 1.5px;
    color: var(--ink);
  }

  /* Back side */
  .card--back {
    background: linear-gradient(135deg, var(--silver-dark), var(--silver-light) 30%, var(--silver-mid) 55%, var(--silver-light) 80%, var(--silver-dark));
    padding: 9px;
    border: 3px solid #2a2a2a;
  }
  .back-panel {
    width: 100%;
    height: 100%;
    border-radius: 16px;
    background: var(--card-black);
    display: flex;
    flex-direction: column;
    align-items: center;
    justify-content: center;
    gap: 6px;
  }
  .contact-line {
    font-family: "Cormorant Garamond", serif;
    font-weight: 500;
    font-size: 21px;
    letter-spacing: 0.6px;
    color: var(--contact-text);
  }
</style>
</head>
<body>
  <main class="canvas">
    <section class="card card--front" aria-label="Front of business card">
      <div class="front-backdrop" role="img" aria-label="Place for a soft silver and white bokeh light photograph"></div>
      <div class="front-frame"></div>
      <div class="front-brand">
        <span class="brand-circle"></span>
        <p class="brand-name">RK Photography</p>
      </div>
    </section>

    <section class="card card--back" aria-label="Back of business card">
      <div class="back-panel">
        <p class="contact-line">(561) 430-2917</p>
        <p class="contact-line">www.rolfkphoto.example</p>
      </div>
    </section>
  </main>
</body>
</html>
```